Fatigued and Overloaded by COVID Messages? We need original illustrations to show that.

Everywhere you look there are messages about COVID. That is leading many people to feel fatigued and overloaded by the messages.

We surveyed U.S. adults March 20th - 24th, 2020 and measured message fatigue, information overload, perceived repetition, and perceived exaggeration. Here is how participants responded:

When it comes to coronavirus . . .
55% feel exhausted by all the messages.
54% feel overloaded by the amount of information.
51% feel that the messages are repetitive.
47% feel like messages exaggerate how bad it is.

In other words, almost half of U.S. adults show signs of message fatigue, information overload, perceived message repetition, and perceived message exaggeration.

We will continue to survey 400 adults every week for the next 16 weeks. Each time we will measure message fatigue, information overload, perceived repetition, and perceived exaggeration. We expect that it will increase over time.

What are we looking for? We need innovative and original illustrations that attempt to communicate these findings. The illustrations would visualize message fatigue, information overload, perceived message repetition, and perceived message exaggeration.

What sort of visual are we looking for? Our preference is for an original illustration (or set of illustrations). Our preference is for creative and powerful illustrations, but we are also open to the creative and well-executed infographics.

We need these images fast . We will award monetary prizes to the 3 best designs. If we like more than that, then we might purchase more (e.g., in past contests, we have purchased as many as 30 designs).

What we will need:
(1) The illustrations must be original and we will need the photoshop and/or illustrator files for all artwork. (By original, we mean that the illustrations are 100% created by you. Our organization requires that we utilize only original illustrated work. We have had issues with free imagery being pirated and reposted as free. We sidestep that issue by just having everything created.)

(2) The illustration should say, somewhere: "Based on a survey of 400 U.S. adults conducted March 20 - 24th, 2020."

(3) We will have almost 4 months worth of data by the time this is done. In other words, the illustrations might be able to help us present that weekly data.

(4) We have conducted other Artvendo projects. It might be helpful to examine designs we liked in the past. For example, here is another COVID project we just finished:

https://jobs.artvendo-example.com/job/5162048

Target Market(s)

U.S. adults

Requirements
Must have
• Original illustrations. Mobile friendly design. People will view this on their smartphones.
Nice to have
• A design that we can use to communicate the data across time.

```html
<!DOCTYPE html>
<html lang="en">
<head>
<meta charset="utf-8">
<title>Information Overload – 54%</title>
<link rel="stylesheet" href="https://fonts.googleapis.com/css2?family=Fira+Sans:ital,wght@0,500;1,500&display=swap">
<style>
  :root {
    --slate: #465159;
    --ground: #32383f;
    --orange: #f39c37;
    --white: #ffffff;
    --umbrella: #f0a03c;
    --coat: #9a9a9a;
    --trousers: #0b3236;
  }
  html, body {
    margin: 0;
    padding: 0;
    overflow: hidden;
    background: var(--slate);
  }
  .poster {
    position: relative;
    width: 1200px;
    height: 1200px;
    overflow: hidden;
    background: var(--slate);
    font-family: "Fira Sans", sans-serif;
    font-weight: 500;
  }
  .word-rain {
    position: absolute;
    inset: 0 0 193px 0;
    overflow: hidden;
  }
  .word-column {
    position: absolute;
    writing-mode: vertical-rl;
    white-space: nowrap;
    overflow: hidden;
    line-height: 1;
    color: var(--orange);
    letter-spacing: -0.01em;
  }
  .ground {
    position: absolute;
    left: 0;
    right: 0;
    top: 1007px;
    bottom: 0;
    background: var(--ground);
  }
  .walker {
    position: absolute;
    left: 438px;
    top: 475px;
    width: 298px;
    height: 547px;
    border-radius: 150px 150px 12px 12px;
    background: linear-gradient(180deg, var(--umbrella) 0%, var(--umbrella) 22%, var(--coat) 40%, var(--coat) 62%, var(--trousers) 80%, var(--trousers) 100%);
  }
  .stat {
    position: absolute;
    left: 648px;
    top: 20px;
    margin: 0;
    font-size: 290px;
    line-height: 1.2;
    color: var(--white);
    letter-spacing: -0.02em;
  }
  .caption {
    position: absolute;
    margin: 0;
    font-style: italic;
    font-size: 92px;
    line-height: 1;
    letter-spacing: -0.01em;
  }
  .caption--information { left: 186px; top: 1012px; color: var(--white); }
  .caption--overload { left: 612px; top: 1086px; color: var(--orange); }
</style>
</head>
<body>
<main class="poster">
  <div class="word-rain" aria-hidden="true">
    <div class="word-column" style="left:8px;top:0;height:125px;font-size:18px">coronavirus coronavirus coronavirus</div>
    <div class="word-column" style="left:8px;top:130px;height:877px;font-size:78px">coronavirus coronavirus coronavirus</div>
    <div class="word-column" style="left:38px;top:40px;height:100px;font-size:12px">coronavirus coronavirus</div>
    <div class="word-column" style="left:60px;top:790px;height:217px;font-size:34px">coronavirus coronavirus coronavirus</div>
    <div class="word-column" style="left:80px;top:35px;height:110px;font-size:14px">coronavirus coronavirus</div>
    <div class="word-column" style="left:98px;top:0;height:380px;font-size:30px">coronavirus coronavirus coronavirus coronavirus</div>
    <div class="word-column" style="left:92px;top:360px;height:647px;font-size:24px">coronavirus coronavirus coronavirus coronavirus coronavirus</div>
    <div class="word-column" style="left:120px;top:370px;height:637px;font-size:58px">coronavirus coronavirus coronavirus</div>
    <div class="word-column" style="left:148px;top:75px;height:300px;font-size:12px">coronavirus coronavirus coronavirus coronavirus coronavirus</div>
    <div class="word-column" style="left:162px;top:30px;height:350px;font-size:12px">coronavirus coronavirus coronavirus coronavirus coronavirus</div>
    <div class="word-column" style="left:178px;top:220px;height:787px;font-size:26px">coronavirus coronavirus coronavirus coronavirus coronavirus coronavirus</div>
    <div class="word-column" style="left:204px;top:30px;height:977px;font-size:60px">coronavirus coronavirus coronavirus coronavirus</div>
    <div class="word-column" style="left:246px;top:560px;height:447px;font-size:24px">coronavirus coronavirus coronavirus coronavirus</div>
    <div class="word-column" style="left:262px;top:40px;height:600px;font-size:24px">coronavirus coronavirus coronavirus coronavirus coronavirus</div>
    <div class="word-column" style="left:268px;top:680px;height:327px;font-size:40px">coronavirus coronavirus</div>
    <div class="word-column" style="left:300px;top:80px;height:600px;font-size:14px">coronavirus coronavirus coronavirus coronavirus coronavirus coronavirus coronavirus coronavirus</div>
    <div class="word-column" style="left:316px;top:90px;height:917px;font-size:26px">coronavirus coronavirus coronavirus coronavirus coronavirus coronavirus coronavirus</div>
    <div class="word-column" style="left:350px;top:380px;height:627px;font-size:40px">coronavirus coronavirus coronavirus coronavirus</div>
    <div class="word-column" style="left:386px;top:20px;height:520px;font-size:44px">coronavirus coronavirus coronavirus</div>
    <div class="word-column" style="left:412px;top:490px;height:517px;font-size:20px">coronavirus coronavirus coronavirus coronavirus coronavirus</div>
    <div class="word-column" style="left:432px;top:60px;height:430px;font-size:16px">coronavirus coronavirus coronavirus coronavirus coronavirus</div>
    <div class="word-column" style="left:455px;top:20px;height:470px;font-size:30px">coronavirus coronavirus coronavirus coronavirus</div>
    <div class="word-column" style="left:490px;top:140px;height:350px;font-size:18px">coronavirus coronavirus coronavirus coronavirus</div>
    <div class="word-column" style="left:512px;top:95px;height:400px;font-size:26px">coronavirus coronavirus coronavirus coronavirus</div>
    <div class="word-column" style="left:545px;top:230px;height:260px;font-size:12px">coronavirus coronavirus coronavirus coronavirus</div>
    <div class="word-column" style="left:562px;top:100px;height:380px;font-size:16px">coronavirus coronavirus coronavirus coronavirus coronavirus</div>
    <div class="word-column" style="left:590px;top:60px;height:410px;font-size:44px">coronavirus coronavirus coronavirus</div>
    <div class="word-column" style="left:640px;top:330px;height:140px;font-size:24px">coronavirus coronavirus</div>
    <div class="word-column" style="left:670px;top:360px;height:100px;font-size:12px">coronavirus coronavirus</div>
    <div class="word-column" style="left:690px;top:300px;height:230px;font-size:12px">coronavirus coronavirus coronavirus coronavirus</div>
    <div class="word-column" style="left:710px;top:300px;height:200px;font-size:24px">coronavirus coronavirus coronavirus</div>
    <div class="word-column" style="left:738px;top:350px;height:657px;font-size:18px">coronavirus coronavirus coronavirus coronavirus coronavirus coronavirus coronavirus</div>
    <div class="word-column" style="left:758px;top:335px;height:672px;font-size:40px">coronavirus coronavirus coronavirus coronavirus</div>
    <div class="word-column" style="left:798px;top:400px;height:607px;font-size:12px">coronavirus coronavirus coronavirus coronavirus coronavirus coronavirus coronavirus coronavirus coronavirus</div>
    <div class="word-column" style="left:812px;top:290px;height:717px;font-size:42px">coronavirus coronavirus coronavirus coronavirus</div>
    <div class="word-column" style="left:852px;top:320px;height:687px;font-size:24px">coronavirus coronavirus coronavirus coronavirus coronavirus coronavirus</div>
    <div class="word-column" style="left:880px;top:350px;height:657px;font-size:40px">coronavirus coronavirus coronavirus coronavirus</div>
    <div class="word-column" style="left:920px;top:460px;height:547px;font-size:14px">coronavirus coronavirus coronavirus coronavirus coronavirus coronavirus coronavirus</div>
    <div class="word-column" style="left:928px;top:295px;height:712px;font-size:26px">coronavirus coronavirus coronavirus coronavirus coronavirus coronavirus</div>
    <div class="word-column" style="left:954px;top:280px;height:727px;font-size:66px">coronavirus coronavirus coronavirus</div>
    <div class="word-column" style="left:1010px;top:560px;height:447px;font-size:12px">coronavirus coronavirus coronavirus coronavirus coronavirus coronavirus</div>
    <div class="word-column" style="left:1026px;top:240px;height:767px;font-size:22px">coronavirus coronavirus coronavirus coronavirus coronavirus coronavirus coronavirus</div>
    <div class="word-column" style="left:1048px;top:290px;height:717px;font-size:24px">coronavirus coronavirus coronavirus coronavirus coronavirus coronavirus</div>
    <div class="word-column" style="left:1076px;top:290px;height:717px;font-size:36px">coronavirus coronavirus coronavirus coronavirus coronavirus</div>
    <div class="word-column" style="left:1112px;top:300px;height:300px;font-size:12px">coronavirus coronavirus coronavirus coronavirus</div>
    <div class="word-column" style="left:1124px;top:660px;height:347px;font-size:20px">coronavirus coronavirus coronavirus</div>
    <div class="word-column" style="left:1128px;top:20px;height:230px;font-size:20px">coronavirus coronavirus coronavirus</div>
    <div class="word-column" style="left:1144px;top:250px;height:757px;font-size:44px">coronavirus coronavirus coronavirus coronavirus</div>
    <div class="word-column" style="left:1172px;top:0;height:1007px;font-size:12px">coronavirus coronavirus coronavirus coronavirus coronavirus coronavirus coronavirus coronavirus coronavirus coronavirus coronavirus coronavirus coronavirus coronavirus coronavirus coronavirus</div>
    <div class="word-column" style="left:1187px;top:0;height:1007px;font-size:12px">coronavirus coronavirus coronavirus coronavirus coronavirus coronavirus coronavirus coronavirus coronavirus coronavirus coronavirus coronavirus coronavirus coronavirus coronavirus coronavirus</div>
  </div>

  <div class="ground"></div>

  <div class="walker" role="img" aria-label="Illustration of a person in a grey hoodie and dark track trousers, carrying a backpack and walking under an orange umbrella through a rain of words"></div>

  <p class="stat">54%</p>
  <p class="caption caption--information">information</p>
  <p class="caption caption--overload">overload</p>
</main>
</body>
</html>
```